Varnell Consulting needs a business card design

Varnell Consulting is a small business that consults and trains Australia wide in Workplace Health and Safety, Environment and Quality Management Systems.

Clients are typically smaller businesses with 50 to 200 employees but there are some large clients.

Communication is often by email, although mobile is used as well.

Varnell Consulting
47 Tessock Downs Road
Marrowdale, QLD 4312
0438 291 604

```html
<!DOCTYPE html>
<html lang="en">
<head>
<meta charset="utf-8">
<title>Varnell Consulting – Business Card</title>
<link rel="stylesheet" href="https://fonts.googleapis.com/css2?family=Josefin+Sans:wght@600&family=Roboto+Condensed:wght@300&display=swap">
<style>
  :root {
    --card-light: #ececec;
    --card-mid: #dcdcdc;
    --card-edge: #c4c4c4;
    --mark-grey: #b3b3b3;
    --ink: #111111;
    --band-red: #e0474a;
  }
  html, body {
    margin: 0;
    padding: 0;
    overflow: hidden;
    background: #ffffff;
  }
  .card {
    position: relative;
    width: 1200px;
    height: 641px;
    overflow: hidden;
    background: radial-gradient(ellipse 75% 85% at 55% 35%, var(--card-light) 0%, var(--card-mid) 60%, var(--card-edge) 100%);
  }
  .brand-disc {
    position: absolute;
    left: 169px;
    top: -15px;
    width: 354px;
    height: 354px;
  }
  .brand-name {
    position: absolute;
    left: 213px;
    top: 116px;
    margin: 0;
    font-family: "Josefin Sans", sans-serif;
    font-weight: 600;
    font-size: 95px;
    line-height: 1;
    letter-spacing: -1px;
    color: var(--ink);
    white-space: nowrap;
  }
  .contact {
    position: absolute;
    left: 0;
    width: 1252px;
    top: 362px;
    margin: 0;
    font-family: "Roboto Condensed", sans-serif;
    font-weight: 300;
    font-style: normal;
    font-size: 34px;
    line-height: 47px;
    color: var(--ink);
    text-align: center;
  }
  .contact span {
    display: block;
  }
  .footer-band {
    position: absolute;
    left: 0;
    top: 505px;
    width: 1200px;
    height: 136px;
    background: var(--band-red);
  }
</style>
</head>
<body>
  <main class="card">
    <svg class="brand-disc" viewBox="0 0 354 354" aria-hidden="true">
      <circle cx="177" cy="177" r="177" fill="var(--mark-grey)"/>
    </svg>
    <h1 class="brand-name">Varnell Consulting</h1>
    <address class="contact">
      <span>47 Tessock Downs Road</span>
      <span>Marrowdale, QLD 4312</span>
      <span>0438 291 604</span>
    </address>
    <div class="footer-band"></div>
  </main>
</body>
</html>
```